Corwenna Foundation is a new grant making charity set up in the UK.

Having got a logo, we now need a website to go with it. We have worked out the text which people are going to need in order to then apply for grants. But having found out what we require they will probably need to go away and think about it.
We have to be careful of what images we use. So I have uploaded some images that we like. We are also going to be adding more pages almost immediately so need to think about the images for these.
I know basic wordpress so I will be able to add new pages/make alterations in future.
Updates
The website does need to be coded in Wordpress so that I can maintain it afterwards.
Corwenna
Brief changed to provide more money and we have also provided more possible pictures. And generally more explanation.
Target Market(s)
departments in universities, other charities doing work on relief of pain, people working in health service departments
Industry/Entity Type
Health Charity
Coding
Coded - Design and coding required
Number of Pages Required
4 page
Look and feel
Each slider illustrates characteristics of the customer's brand and the style your logo design should communicate.

```html
<!DOCTYPE html>
<html lang="en">
<head>
<meta charset="utf-8">
<title>Corwenna Foundation</title>
<link href="https://fonts.googleapis.com/css2?family=Roboto:wght@400;500;700;900&display=swap" rel="stylesheet">
<style>
:root{
  --blue:#0a6dbf;
  --blue-dark:#0b4f8f;
  --ink:#111;
  --text:#666;
  --grey-band:#7a7a7a;
  --light:#f3f3f3;
  --footer:#3b3b3b;
  --line:#dde3ea;
  --white:#fff;
}
*{margin:0;padding:0;box-sizing:border-box}
html,body{width:1200px;height:3154px;overflow:hidden}
body{position:relative;font-family:'Roboto',sans-serif;background:var(--white);color:var(--ink)}
.abs{position:absolute}
.btn{position:absolute;display:flex;align-items:center;justify-content:center;gap:10px;border-radius:22px;font-weight:700;font-size:14px;text-transform:uppercase}
.btn-solid{background:var(--blue);color:var(--white)}
.btn-line{border:2px solid var(--blue);color:var(--blue);background:var(--white)}

/* header */
.site-header{position:absolute;left:0;top:0;width:1200px;height:83px;background:var(--white);border-top:3px solid var(--blue)}
.brand{position:absolute;left:114px;top:23px;display:flex;align-items:center;gap:9px;font-weight:700;font-size:21px;color:var(--blue);white-space:nowrap;max-width:270px}
.brand-mark{width:34px;height:34px;border:3px solid var(--blue);flex:none}
.nav{position:absolute;top:36px;font-size:14px;font-weight:500;color:var(--ink)}

/* hero */
.hero{position:absolute;left:0;top:83px;width:1200px;height:620px}
.hero-bg{position:absolute;inset:0;background:radial-gradient(ellipse at 75% 45%,#3f7fe0 0%,#1d4da3 30%,#0c2a66 60%,#071838 100%)}
.hero-kicker{left:113px;top:208px;font-size:22px;font-weight:700;color:var(--white)}
.hero-title{left:113px;top:246px;font-size:61px;line-height:64px;font-weight:900;color:var(--white)}
.hero-lead{left:113px;top:394px;width:460px;font-size:16.5px;line-height:22px;color:var(--white)}
.slide-btn{position:absolute;top:538px;width:40px;height:32px;border:1px solid #cfd8e6;display:flex;align-items:center;justify-content:center}

/* sections */
.section-title{position:absolute;left:0;width:1200px;text-align:center;font-weight:900;font-size:34px}
.grants-intro{position:absolute;left:160px;top:826px;width:880px;text-align:center;font-size:14px;line-height:24px;color:var(--text)}
.card{position:absolute;width:306px;height:191px;border:1px solid var(--line);background:var(--white)}
.card-icon{position:absolute;width:76px;height:76px;background:var(--blue);display:flex;align-items:center;justify-content:center}
.card h3{position:absolute;left:24px;top:72px;font-size:13.5px;font-weight:700;text-transform:uppercase}
.card p{position:absolute;left:24px;top:94px;width:270px;font-size:13.5px;line-height:24px;color:var(--text)}

.about-title{left:680px;top:1710px;font-size:37px;font-weight:900;color:var(--blue)}
.about-text{left:680px;width:390px;font-size:14.5px;line-height:25.7px;color:var(--text)}

.post-date{position:absolute;background:var(--blue);color:var(--white);font-size:13.5px;font-weight:700;display:flex;align-items:center;justify-content:center}
.post-title{position:absolute;font-size:17px;line-height:23px;font-weight:900;text-transform:uppercase}
.post-text{position:absolute;font-size:14.5px;line-height:19px;color:var(--text)}

/* footer */
.site-footer{position:absolute;left:0;top:2766px;width:1200px;height:337px;background:var(--footer);color:var(--white)}
.foot-brand{left:111px;top:91px;display:flex;align-items:center;gap:8px;font-size:27px;font-weight:500}
.foot-brand .brand-mark{border-color:var(--white)}
.foot-icon{position:absolute;width:40px;height:40px;border:2px solid var(--white);border-radius:50%;display:flex;align-items:center;justify-content:center}
.foot-head{position:absolute;top:78px;font-size:14px;font-weight:700;text-transform:uppercase}
.foot-rule{position:absolute;top:102px;width:279px;height:1px;background:#9a9a9a}
.foot-link{position:absolute;font-size:14.5px;display:flex;gap:16px}
.foot-link span:first-child{font-size:12px;line-height:18px}
.news-input{position:absolute;left:768px;top:167px;width:285px;height:46px;background:var(--white);color:#777;font-size:14px;padding:14px 17px}
.news-send{position:absolute;left:1010px;top:167px;width:43px;height:46px;background:var(--blue);display:flex;align-items:center;justify-content:center}
.social{position:absolute;top:242px;width:36px;height:36px;border:2px solid var(--white);border-radius:50%}
.copyright{position:absolute;left:0;top:3103px;width:1200px;height:51px;background:var(--blue);color:var(--white);font-size:14.5px;display:flex;align-items:center;justify-content:center}
</style>
</head>
<body>

<header class="site-header">
  <div class="brand"><span class="brand-mark"></span>Corwenna Foundation</div>
  <span class="nav" style="left:408px">HOME</span>
  <span class="nav" style="left:481px">ABOUT US</span>
  <span class="nav" style="left:584px">GRANTS</span>
  <span class="nav" style="left:673px">LATEST BLOG</span>
  <span class="nav" style="left:798px">CONTACT US</span>
  <a class="btn btn-solid" style="left:940px;top:20px;width:147px;height:43px">Get Started
    <svg width="14" height="14" viewBox="0 0 14 14"><circle cx="7" cy="7" r="7" fill="#fff"/><path d="M4 7h5M7 4.5 9.5 7 7 9.5" stroke="#0a6dbf" stroke-width="1.8" fill="none"/></svg></a>
</header>

<section class="hero">
  <div class="hero-bg" role="img" aria-label="Glowing blue network of nerve cells"></div>
  <svg class="abs" style="left:0;top:0" width="1200" height="620" viewBox="0 0 1200 620">
    <polygon points="0,610 1200,540 1200,620 0,620" fill="#fff"/>
    <polygon points="600,572 1200,535 1200,554 600,594" fill="#0a6dbf"/>
    <polygon points="508,578 582,573 582,601 508,605" fill="#7a7a7a"/>
  </svg>
</section>
<div class="abs hero-kicker">WELCOME TO</div>
<div class="abs hero-title">CORWENNA<br>FOUNDATION</div>
<p class="abs hero-lead">The main aim of Corwenna Foundation is to reduce the suffering caused by chronic pain.</p>
<a class="btn btn-solid" style="left:113px;top:463px;width:148px;height:43px">Get Started
  <svg width="14" height="14" viewBox="0 0 14 14"><circle cx="7" cy="7" r="7" fill="#fff"/><path d="M4 7h5M7 4.5 9.5 7 7 9.5" stroke="#0a6dbf" stroke-width="1.8" fill="none"/></svg></a>
<div class="slide-btn" style="left:113px"><svg width="22" height="8"><path d="M1 4h20M5 1 1 4l4 3" stroke="#fff" stroke-width="1.5" fill="none"/></svg></div>
<div class="slide-btn" style="left:159px;background:#8d97a6"><svg width="22" height="8"><path d="M1 4h20M17 1l4 3-4 3" stroke="#fff" stroke-width="1.5" fill="none"/></svg></div>

<h2 class="section-title" style="top:760px;color:var(--blue)">GRANTS</h2>
<p class="grants-intro">Grants will almost entirely be provided for research or education into pain management, or the prevention of pain.The trustees will also be providing grants to a number of other charities or to areas with which they have had a long term association, such as HIV/AIDS and TB. There is no application procedure for these other areas, and unsolicited applications are unlikely to be favorably considered by the trustees<br>The main categories of funding for pain research or education will be as follows</p>

<div class="card" style="left:113px;top:993px"><h3>Pain Centres</h3><p>Lorem ipsum dolor sit amet, consectetur adipiscing elit, sed do eiusmod tempor incididunt ut labore et dolore magna</p></div>
<div class="card" style="left:457px;top:993px"><h3>The Use of Opioids</h3><p>Lorem ipsum dolor sit amet, consectetur adipiscing elit, sed do eiusmod tempor incididunt ut labore et dolore magna</p></div>
<div class="card" style="left:800px;top:993px"><h3>Improving the Use of Medication</h3><p>Lorem ipsum dolor sit amet, consectetur adipiscing elit, sed do eiusmod tempor incididunt ut labore et dolore magna</p></div>
<div class="card" style="left:113px;top:1259px"><h3>Education</h3><p>Lorem ipsum dolor sit amet, consectetur adipiscing elit, sed do eiusmod tempor incididunt ut labore et dolore magna</p></div>
<div class="card" style="left:457px;top:1259px"><h3>Improved Types of Pain Control</h3><p>Lorem ipsum dolor sit amet, consectetur adipiscing elit, sed do eiusmod tempor incididunt ut labore et dolore magna</p></div>
<div class="card" style="left:800px;top:1259px"><h3>Measuring Pain</h3><p>Lorem ipsum dolor sit amet, consectetur adipiscing elit, sed do eiusmod tempor incididunt ut labore et dolore magna</p></div>

<div class="card-icon" style="left:146px;top:955px"><svg width="40" height="40" viewBox="0 0 40 40"><rect x="2" y="2" width="36" height="36" rx="6" fill="#fff"/><path d="M11 13h18M11 19h18M11 25h18M11 31h12" stroke="#0a6dbf" stroke-width="2.5"/></svg></div>
<div class="card-icon" style="left:489px;top:955px"><svg width="48" height="40" viewBox="0 0 48 40" fill="#fff"><circle cx="24" cy="9" r="6"/><circle cx="12" cy="12" r="4"/><circle cx="36" cy="12" r="4"/><path d="M4 30l10-8 8 4 6-4 8 2 8 6-10 8-10-4-10 4z"/></svg></div>
<div class="card-icon" style="left:833px;top:955px"><svg width="34" height="42" viewBox="0 0 34 42"><path d="M2 2h22l8 8v30H2z" fill="#fff"/><path d="M9 8v8M5 12h8M8 22h18M8 28h18M8 34h12" stroke="#0a6dbf" stroke-width="2.5"/></svg></div>
<div class="card-icon" style="left:146px;top:1221px"><svg width="44" height="40" viewBox="0 0 44 40" fill="#fff"><circle cx="9" cy="9" r="5"/><path d="M3 18h12l8-4 2 3-8 5v16H4z"/><rect x="20" y="4" width="22" height="16" fill="none" stroke="#fff" stroke-width="2.5"/><path d="M28 20l-4 16M34 20l4 16" stroke="#fff" stroke-width="2.5"/></svg></div>
<div class="card-icon" style="left:489px;top:1221px"><svg width="46" height="40" viewBox="0 0 46 40" fill="#fff"><circle cx="16" cy="7" r="5"/><circle cx="30" cy="9" r="4"/><rect x="4" y="18" width="38" height="20" rx="2"/><path d="M10 24h26M10 30h26" stroke="#0a6dbf" stroke-width="2"/></svg></div>
<div class="card-icon" style="left:833px;top:1221px"><svg width="48" height="30" viewBox="0 0 48 30"><path d="M2 2v14M46 2v14M4 9h40M8 6 4 9l4 3M40 6l4 3-4 3" stroke="#fff" stroke-width="2.5" fill="none"/><rect x="2" y="19" width="44" height="9" fill="#fff"/></svg></div>

<!-- about -->
<svg class="abs" style="left:0;top:1570px" width="1200" height="540" viewBox="0 0 1200 540">
  <polygon points="0,70 1200,0 1200,540 0,540" fill="#f3f3f3"/>
  <polygon points="0,65 600,25 600,50 0,88" fill="#0a6dbf"/>
  <polygon points="617,24 692,20 692,44 617,48" fill="#7a7a7a"/>
</svg>
<div class="abs" role="img" aria-label="Illustration of a crowd of colourful people silhouettes" style="left:0;top:1782px;width:661px;height:324px;background:linear-gradient(90deg,#d18a2c 0%,#9a2d34 35%,#b93a3a 60%,#d9c6a8 90%,#f3f3f3 100%)"></div>
<h2 class="abs about-title">ABOUT US</h2>
<svg class="abs" style="left:857px;top:1729px" width="230" height="272"><path d="M61 2H227V268H0" stroke="#0a6dbf" stroke-width="3" fill="none"/></svg>
<p class="abs about-text" style="top:1764px">The medical advisers are doctors or other professionals, who individually or collectively advise the trustees on the merit of grant applications. Medical advisers are initially appointed for a five year term.</p>
<p class="abs about-text" style="top:1877px">It is unclear how much money the Foundation will have in a few years time, but currently it has about a million poundsIt is unclear how much money</p>
<a class="btn btn-line" style="left:680px;top:1976px;width:148px;height:43px">Learn More
  <svg width="14" height="14" viewBox="0 0 14 14"><circle cx="7" cy="7" r="7" fill="#0a6dbf"/><path d="M4 7h5M7 4.5 9.5 7 7 9.5" stroke="#fff" stroke-width="1.8" fill="none"/></svg></a>

<!-- blog -->
<h2 class="section-title" style="top:2176px">LATEST BLOG POST</h2>
<div class="abs" style="left:111px;top:2460px;width:45px;height:81px;background:#0e1a2e"></div>
<div class="abs" role="img" aria-label="Blue glowing nerve cells" style="left:111px;top:2268px;width:446px;height:232px;background:radial-gradient(ellipse at 60% 50%,#3c8ee8,#0f3f8a 70%,#0a2450)"></div>
<div class="post-date" style="left:185px;top:2486px;width:120px;height:32px">01 OCT , 2021</div>
<div class="post-title" style="left:186px;top:2541px;width:360px">Lorem ipsum dolor sit amet consec tetur adipiscing</div>
<p class="post-text" style="left:186px;top:2597px;width:340px">Sed ut perspiciatis unde omnis iste natus error sit voluptatem accusantium dolorem</p>

<div class="abs" role="img" aria-label="Hand holding a glowing nerve network" style="left:572px;top:2268px;width:251px;height:195px;background:radial-gradient(ellipse at 45% 60%,#d9a0c0,#a9c8e6 45%,#eef3f8)"></div>
<div class="post-date" style="left:846px;top:2287px;width:121px;height:37px">01 OCT , 2021</div>
<div class="post-title" style="left:847px;top:2344px;width:290px">Lorem ipsum dolor sit amet tetur adipiscing</div>
<p class="post-text" style="left:847px;top:2400px;width:290px">Sed ut perspiciatis unde omnis iste natus error sit voluptatem accusantium</p>

<div class="abs" role="img" aria-label="Hands reaching toward a glowing brain at sunset" style="left:572px;top:2478px;width:251px;height:195px;background:linear-gradient(180deg,#6f6a66 0%,#c68a48 55%,#f1b055 75%,#3a2a1e 100%)"></div>
<div class="post-date" style="left:846px;top:2498px;width:121px;height:37px">01 OCT , 2021</div>
<div class="post-title" style="left:847px;top:2555px;width:290px">Lorem ipsum dolor sit amet tetur adipiscing</div>
<p class="post-text" style="left:847px;top:2611px;width:290px">Sed ut perspiciatis unde omnis iste natus error sit voluptatem accusantium</p>

<footer class="site-footer">
  <div class="abs foot-brand"><span class="brand-mark"></span>CORWENNA</div>
  <div class="foot-icon" style="left:111px;top:169px"><svg width="14" height="20" viewBox="0 0 14 20"><path d="M7 19S1 11 1 7a6 6 0 0 1 12 0c0 4-6 12-6 12z" fill="none" stroke="#fff" stroke-width="2"/><circle cx="7" cy="7" r="2" fill="#fff"/></svg></div>
  <p class="abs" style="left:173px;top:168px;font-size:14.5px;line-height:22px">191 , Lorem ipsum dolor sit<br>United Kingdom</p>
  <div class="foot-icon" style="left:111px;top:223px"><svg width="18" height="18" viewBox="0 0 18 18"><path d="M4 1l3 4-2 2c1 3 3 5 6 6l2-2 4 3-2 3C7 17 1 11 1 3z" fill="#fff"/></svg></div>
  <p class="abs" style="left:173px;top:234px;font-size:14.5px">1 555 010 010</p>

  <div class="foot-head" style="left:416px">Links</div>
  <div class="foot-rule" style="left:416px"></div>
  <div class="foot-link" style="left:416px;top:126px"><span>»</span><span>Home</span></div>
  <div class="foot-link" style="left:416px;top:160px"><span>»</span><span>About us</span></div>
  <div class="foot-link" style="left:416px;top:194px"><span>»</span><span>Grants</span></div>
  <div class="foot-link" style="left:416px;top:228px"><span>»</span><span>Testimonials</span></div>
  <div class="foot-link" style="left:416px;top:262px"><span>»</span><span>Blog</span></div>
  <div class="foot-link" style="left:588px;top:126px"><span>»</span><span>FAQ</span></div>
  <div class="foot-link" style="left:588px;top:160px"><span>»</span><span>Sitemap</span></div>
  <div class="foot-link" style="left:588px;top:194px"><span>»</span><span>Privacy Policy</span></div>
  <div class="foot-link" style="left:588px;top:228px"><span>»</span><span>Terms Of Use</span></div>
  <div class="foot-link" style="left:588px;top:262px"><span>»</span><span>Contact Us</span></div>

  <div class="foot-head" style="left:767px">Newsletter</div>
  <div class="foot-rule" style="left:767px"></div>
  <p class="abs" style="left:768px;top:130px;font-size:14.5px">Send us a newsletter to get update</p>
  <div class="news-input">Email Address</div>
  <div class="news-send"><svg width="16" height="16" viewBox="0 0 16 16"><path d="M15 1 1 7l5 2 2 6z M6 9l9-8" fill="none" stroke="#fff" stroke-width="1.5"/></svg></div>
  <div class="social" style="left:768px"></div>
  <div class="social" style="left:811px"></div>
  <div class="social" style="left:854px"></div>
  <div class="social" style="left:897px"></div>
</footer>
<div class="copyright">© 2021 Corwenna Foundation. All Rights Reserved</div>

</body>
</html>
```